Numbrella : This is a Puzzle and This is not a Puzzle

Numbrella is a new addictive way to play Sudoku (see description on the attached document).
We would like your help in developing a design for the playscreen of the game (a mock-up is in the attached document)
The winner will be entrusted with the work of the complete design of the application (home screen, configuration screen, etc.) in a specific contract.
Thank you from Paris France.
Best.
Anselme

```html
<!DOCTYPE html>
<html lang="en">
<head>
<meta charset="utf-8">
<title>Puzzle game — Play screen</title>
<link rel="stylesheet" href="https://fonts.googleapis.com/css2?family=Jost:wght@300;400&display=swap">
<style>
  :root {
    --bg: #ffffff;
    --ink: #111111;
    --grid-line: #0f1a2e;
    --card-line: #c8c8c8;
    --level-bg: #e2f4dc;
    --yellow: #fddc5c;
    --cyan: #5fe0e3;
    --green: #7ed957;
    --purple: #cb6ce6;
    --orange: #ff914d;
    --red: #ff5757;
    --teal: #0097b2;
    --eye-cyan: #5ce1e6;
  }
  html, body {
    margin: 0;
    width: 1200px;
    height: 1200px;
    overflow: hidden;
    background: var(--bg);
  }
  .play-screen {
    position: absolute;
    left: 39px;
    top: 341px;
    width: 1122px;
    height: 517px;
  }
  .play-screen svg { display: block; width: 100%; height: 100%; }
  .digit { font-family: "Jost", sans-serif; font-weight: 300; fill: var(--ink); text-anchor: middle; dominant-baseline: central; }
  .digit--large { font-size: 42px; }
  .digit--small { font-size: 14px; }
  .stars { font-family: "Jost", sans-serif; font-size: 24px; fill: var(--ink); dominant-baseline: central; }
  .card { fill: var(--bg); stroke: var(--card-line); stroke-width: 2; }
  .card--level { fill: var(--level-bg); }
  .board line, .board rect { stroke: var(--grid-line); stroke-width: 2; fill: none; }
  .number-pad rect { fill: var(--bg); stroke: var(--ink); stroke-width: 2; }
  .nav-button { fill: #1a1a1a; }
  .outline-icon { fill: none; stroke: var(--ink); stroke-width: 4; stroke-linecap: round; stroke-linejoin: round; }
</style>
</head>
<body>
<main class="play-screen">
  <svg viewBox="140 685 1650 760" xmlns="http://www.w3.org/2000/svg" aria-label="Puzzle game play screen">
    <!-- Player card -->
    <g class="player-card">
      <rect class="card" x="213" y="710" width="227" height="45" rx="6"/>
      <circle cx="237" cy="733" r="15" fill="var(--ink)"/>
      <circle cx="237" cy="733" r="11" fill="none" stroke="#fff" stroke-width="1.5"/>
      <circle cx="237" cy="729" r="4" fill="none" stroke="#fff" stroke-width="1.5"/>
      <path d="M230 740 q7 -8 14 0" fill="none" stroke="#fff" stroke-width="1.5"/>
      <text class="stars" x="273" y="734">★ ★ ★ ☆ ☆</text>
    </g>
    <!-- Level card -->
    <g class="level-card">
      <rect class="card card--level" x="213" y="768" width="227" height="45" rx="6"/>
      <g fill="var(--ink)">
        <rect x="224" y="777" width="8" height="8"/><rect x="233" y="777" width="8" height="8"/><rect x="242" y="777" width="8" height="8"/>
        <rect x="224" y="786" width="8" height="8"/><rect x="233" y="786" width="8" height="8"/><rect x="242" y="786" width="8" height="8"/>
        <rect x="224" y="795" width="8" height="8"/><rect x="233" y="795" width="8" height="8"/><rect x="242" y="795" width="8" height="8"/>
      </g>
      <g stroke="var(--ink)" stroke-width="1.5">
        <circle cx="285" cy="790" r="8" fill="#dddddd"/>
        <circle cx="312" cy="790" r="8" fill="#aaaaaa"/>
        <circle cx="340" cy="790" r="8" fill="#777777"/>
        <circle cx="368" cy="790" r="8" fill="#444444"/>
        <circle cx="396" cy="790" r="8" fill="#ffffff"/>
      </g>
    </g>
    <!-- Previous -->
    <g class="nav-previous">
      <circle class="nav-button" cx="252" cy="1063" r="48"/>
      <path d="M218 1063 l26 -18 v36 z M246 1063 l26 -18 v36 z" fill="#fff"/>
    </g>
    <!-- Colour view toggle -->
    <g class="colour-view">
      <rect x="216" y="1171" width="30" height="30" fill="var(--yellow)"/>
      <rect x="246" y="1171" width="30" height="30" fill="var(--purple)"/>
      <rect x="276" y="1171" width="30" height="30" fill="var(--yellow)"/>
      <rect x="216" y="1201" width="30" height="31" fill="var(--cyan)"/>
      <rect x="246" y="1201" width="30" height="31" fill="var(--orange)"/>
      <rect x="276" y="1201" width="30" height="31" fill="var(--green)"/>
      <rect x="216" y="1232" width="30" height="30" fill="var(--green)"/>
      <rect x="246" y="1232" width="30" height="30" fill="var(--red)"/>
      <rect x="276" y="1232" width="30" height="30" fill="var(--teal)"/>
      <path d="M204 1170 q16 -14 32 0 q-16 14 -32 0z" fill="var(--eye-cyan)"/>
      <circle cx="220" cy="1170" r="5" fill="#fff"/><circle cx="220" cy="1170" r="3" fill="var(--eye-cyan)"/>
    </g>
    <!-- Colour hint -->
    <g class="hint-colour" stroke="var(--yellow)" stroke-width="4" stroke-linecap="round">
      <line x1="252" y1="1294" x2="252" y2="1302"/>
      <line x1="214" y1="1315" x2="221" y2="1319"/><line x1="290" y1="1315" x2="283" y2="1319"/>
      <line x1="214" y1="1358" x2="221" y2="1354"/><line x1="290" y1="1358" x2="283" y2="1354"/>
      <path d="M252 1313 a24 24 0 0 1 14 43 l-4 24 h-20 l-4 -24 a24 24 0 0 1 14 -43z" fill="var(--yellow)" stroke="none"/>
      <rect x="243" y="1385" width="18" height="12" fill="var(--yellow)" stroke="none"/>
    </g>
    <!-- Colour eraser -->
    <g class="eraser-colour">
      <path d="M340 1295 l26 -30 l56 48 l-26 30 z" fill="var(--purple)"/>
      <path d="M372 1316 l22 -26 l26 22 q4 6 0 12 l-12 16 h-20 z" fill="#fff" stroke="var(--purple)" stroke-width="4" stroke-linejoin="round"/>
      <line x1="338" y1="1342" x2="410" y2="1342" stroke="var(--purple)" stroke-width="4" stroke-linecap="round"/>
      <path d="M418 1342 h14 M424 1332 l6 -10" stroke="var(--purple)" stroke-width="3" stroke-linecap="round"/>
    </g>
    <!-- Colour palette -->
    <g class="colour-palette">
      <rect x="466" y="730" width="73" height="75" fill="var(--yellow)"/>
      <rect x="466" y="804" width="73" height="75" fill="var(--cyan)"/>
      <rect x="466" y="878" width="73" height="75" fill="var(--green)"/>
      <rect x="466" y="952" width="73" height="75" fill="var(--purple)"/>
      <rect x="466" y="1026" width="73" height="75" fill="var(--orange)"/>
      <rect x="466" y="1100" width="73" height="75" fill="var(--red)"/>
      <rect x="466" y="1174" width="73" height="75" fill="var(--yellow)"/>
      <rect x="466" y="1248" width="73" height="75" fill="var(--green)"/>
      <rect x="466" y="1322" width="73" height="75" fill="var(--teal)"/>
    </g>
    <!-- Board -->
    <g class="board">
      <rect x="614" y="710" width="708" height="707"/>
      <line x1="693" y1="710" x2="693" y2="1417"/><line x1="771" y1="710" x2="771" y2="1417"/>
      <line x1="850" y1="710" x2="850" y2="1417"/><line x1="929" y1="710" x2="929" y2="1417"/>
      <line x1="1007" y1="710" x2="1007" y2="1417"/><line x1="1086" y1="710" x2="1086" y2="1417"/>
      <line x1="1165" y1="710" x2="1165" y2="1417"/><line x1="1243" y1="710" x2="1243" y2="1417"/>
      <line x1="614" y1="789" x2="1322" y2="789"/><line x1="614" y1="867" x2="1322" y2="867"/>
      <line x1="614" y1="946" x2="1322" y2="946"/><line x1="614" y1="1024" x2="1322" y2="1024"/>
      <line x1="614" y1="1103" x2="1322" y2="1103"/><line x1="614" y1="1181" x2="1322" y2="1181"/>
      <line x1="614" y1="1260" x2="1322" y2="1260"/><line x1="614" y1="1338" x2="1322" y2="1338"/>
    </g>
    <!-- Number pad -->
    <g class="number-pad">
      <rect x="1398" y="730" width="71" height="668"/>
      <g stroke="var(--ink)" stroke-width="2">
        <line x1="1398" y1="804" x2="1469" y2="804"/><line x1="1398" y1="879" x2="1469" y2="879"/>
        <line x1="1398" y1="953" x2="1469" y2="953"/><line x1="1398" y1="1027" x2="1469" y2="1027"/>
        <line x1="1398" y1="1101" x2="1469" y2="1101"/><line x1="1398" y1="1175" x2="1469" y2="1175"/>
        <line x1="1398" y1="1250" x2="1469" y2="1250"/><line x1="1398" y1="1324" x2="1469" y2="1324"/>
      </g>
      <text class="digit digit--large" x="1433" y="767">1</text>
      <text class="digit digit--large" x="1433" y="841">2</text>
      <text class="digit digit--large" x="1433" y="915">3</text>
      <text class="digit digit--large" x="1433" y="989">4</text>
      <text class="digit digit--large" x="1433" y="1063">5</text>
      <text class="digit digit--large" x="1433" y="1137">6</text>
      <text class="digit digit--large" x="1433" y="1211">7</text>
      <text class="digit digit--large" x="1433" y="1286">8</text>
      <text class="digit digit--large" x="1433" y="1360">9</text>
    </g>
    <!-- Home -->
    <g class="nav-home">
      <circle class="nav-button" cx="1690" cy="757" r="48"/>
      <path d="M1656 760 l34 -30 l34 30" fill="none" stroke="#fff" stroke-width="6" stroke-linejoin="round"/>
      <path d="M1665 758 v30 h50 v-30" fill="none" stroke="#fff" stroke-width="6"/>
      <rect x="1684" y="774" width="12" height="16" fill="#fff"/>
      <rect x="1710" y="732" width="7" height="14" fill="#fff"/>
    </g>
    <!-- Timer -->
    <g class="timer">
      <circle class="outline-icon" cx="1695" cy="893" r="38"/>
      <circle cx="1695" cy="893" r="31" fill="none" stroke="var(--ink)" stroke-width="1.5" stroke-dasharray="3 9"/>
      <path class="outline-icon" d="M1695 855 v-10 M1684 845 h22 M1724 868 l8 -8" />
      <path d="M1695 875 v20 h12" fill="none" stroke="var(--ink)" stroke-width="2.5"/>
      <path class="outline-icon" d="M1648 874 h14 M1645 886 h12 M1645 898 h12 M1648 910 h14 M1656 922 h16" stroke-width="2.5"/>
    </g>
    <!-- Next -->
    <g class="nav-next">
      <circle class="nav-button" cx="1690" cy="1063" r="48"/>
      <path d="M1724 1063 l-26 -18 v36 z M1696 1063 l-26 -18 v36 z" fill="#fff"/>
    </g>
    <!-- Number view toggle -->
    <g class="number-view">
      <rect x="1656" y="1172" width="85" height="89" fill="#fff" stroke="var(--ink)" stroke-width="2"/>
      <g stroke="var(--ink)" stroke-width="1.5">
        <line x1="1684" y1="1172" x2="1684" y2="1261"/><line x1="1713" y1="1172" x2="1713" y2="1261"/>
        <line x1="1656" y1="1202" x2="1741" y2="1202"/><line x1="1656" y1="1231" x2="1741" y2="1231"/>
      </g>
      <text class="digit digit--small" x="1670" y="1187">1</text><text class="digit digit--small" x="1699" y="1187">4</text><text class="digit digit--small" x="1727" y="1187">7</text>
      <text class="digit digit--small" x="1670" y="1217">2</text><text class="digit digit--small" x="1699" y="1217">5</text><text class="digit digit--small" x="1727" y="1217">8</text>
      <text class="digit digit--small" x="1670" y="1246">3</text><text class="digit digit--small" x="1699" y="1246">6</text><text class="digit digit--small" x="1727" y="1246">9</text>
      <path d="M1638 1170 q17 -15 34 0 q-17 15 -34 0z" fill="var(--ink)"/>
      <circle cx="1655" cy="1170" r="5" fill="#fff"/><circle cx="1655" cy="1170" r="3" fill="var(--ink)"/>
    </g>
    <!-- Number eraser -->
    <g class="eraser-number">
      <path d="M1548 1272 l32 -22 q6 -2 10 2 l10 12 q3 6 -2 10 l-30 26 z" fill="var(--ink)"/>
      <path d="M1548 1272 l20 28 l-14 12 q-6 4 -12 0 l-20 -14 q-4 -4 0 -10 z" fill="#fff" stroke="var(--ink)" stroke-width="4" stroke-linejoin="round"/>
      <line x1="1520" y1="1330" x2="1602" y2="1330" stroke="var(--ink)" stroke-width="4" stroke-linecap="round"/>
      <path d="M1508 1330 h10 M1508 1312 l6 8" stroke="var(--ink)" stroke-width="3" stroke-linecap="round"/>
    </g>
    <!-- Number hint -->
    <g class="hint-number">
      <path class="outline-icon" d="M1690 1312 a24 24 0 0 1 14 43 l-4 22 h-20 l-4 -22 a24 24 0 0 1 14 -43z" stroke-width="3"/>
      <rect class="outline-icon" x="1681" y="1380" width="18" height="13" rx="3" stroke-width="3"/>
      <path class="outline-icon" d="M1690 1294 v8 M1652 1315 l7 4 M1728 1315 l-7 4 M1652 1358 l7 -4 M1728 1358 l-7 -4" stroke-width="3"/>
    </g>
  </svg>
</main>
</body>
</html>
```